Business Card Design

Quorvel Software Limited develops and sells venue and event management software called Quorvel Stagehand, which is available in the cloud or on-premise. The company was established in 1986. Most of our customers are performing arts venues, museums and festivals. Our existing design is a bit dull. We need to convey that we are both innovative and reliable.
Not all our people show their mobile phone numbers on their cards, so the design needs to work land line and mobile or land line only.

Industry/Entity Type

Software

Contact Information for Business Card

Helen Trasko
Director
Quorvel Software Limited
42B Milbrook Lane, Epsom, Surrey, KT19 4DN
Telephone: +44 (0)1372 640913
Mobile: +44 (0)7945 216804
Email: htrasko@quorvel.net
Web: www.quorvel.net

```html
<!DOCTYPE html>
<html lang="en">
<head>
<meta charset="utf-8">
<title>Quorvel Software Limited – Helen Trasko</title>
<link href="https://fonts.googleapis.com/css2?family=Marcellus+SC&display=swap" rel="stylesheet">
<style>
  :root {
    --navy: #2a4466;
    --blue: #4a6fa0;
    --grey: #c3c4c6;
    --white: #ffffff;
    --name-ink: #d9dce2;
    --contact-ink: #24405f;
  }
  * { margin: 0; padding: 0; box-sizing: border-box; }
  html, body {
    width: 1200px; height: 777px; overflow: hidden; background: var(--white);
  }
  .card {
    position: relative; width: 1200px; height: 777px;
    font-family: "Marcellus SC", "Times New Roman", serif;
  }
  .panel { position: absolute; }
  .panel--left { left: 0; top: 0; width: 660px; height: 777px; background: var(--navy); }
  .panel--brand {
    left: 0; top: 275px; width: 660px; height: 215px; background: var(--white);
    display: flex; align-items: center; justify-content: center; gap: 28px;
  }
  .panel--identity {
    left: 660px; top: 0; width: 540px; height: 497px; background: var(--blue);
  }
  .panel--contact {
    left: 660px; top: 497px; width: 540px; height: 280px; background: var(--grey);
  }
  .brand-mark { width: 46px; height: 46px; background: var(--blue); }
  .brand-name {
    color: var(--navy); font-size: 74px; letter-spacing: 4px; line-height: 1;
  }
  .identity {
    position: absolute; left: 0; right: 0; top: 322px; text-align: center; color: var(--name-ink);
  }
  .identity__name { font-size: 54px; letter-spacing: 3px; line-height: 1; }
  .identity__role { font-size: 38px; letter-spacing: 2px; line-height: 1; margin-top: 14px; }
  .contact {
    position: absolute; left: 0; right: 0; top: 38px; text-align: center;
    color: var(--contact-ink); font-size: 26px; letter-spacing: 1px; line-height: 30px;
  }
  .contact__address { margin-bottom: 14px; }
</style>
</head>
<body>
  <div class="card">
    <div class="panel panel--left"></div>
    <div class="panel panel--brand">
      <span class="brand-mark" aria-hidden="true"></span>
      <span class="brand-name">QUORVEL</span>
    </div>
    <div class="panel panel--identity">
      <div class="identity">
        <p class="identity__name">Helen Trasko</p>
        <p class="identity__role">Director</p>
      </div>
    </div>
    <div class="panel panel--contact">
      <div class="contact">
        <p class="contact__address">42B Milbrook Lane, Epsom, Surrey,<br>KT19 4DN</p>
        <p class="contact__line">Telephone: +44 (0)1372 640913</p>
        <p class="contact__line">Mobile: +44 (0)7945 216804</p>
        <p class="contact__line">Email: htrasko@quorvel.net</p>
        <p class="contact__line">Web: www.quorvel.net</p>
      </div>
    </div>
  </div>
</body>
</html>
```